Baby acupressure app for parents

We need an app for parents that teaches parents how to help them relieve their baby's imbalances (stomach ache, trouble sleeping etc.)

Please see the attached document (with info) and wireframes.

This project is urgent so please only participate if you're able to finish all screens within a few days after the contest is over.

Target Market(s)

Baby moms (20-40 years of age)

Industry/Entity Type

Baby Care

Colors
886aae
b768aa
e667a6
f68d4d
faa54b
fac994
f9ba93
f59195
fee18a

Requirements
Must have
• A high quality design that is both modern and very sleek and stylish.
Nice to have
• Simple animations to make the app "feel" like it's extreme high quality and make the user want to use it again and again
Should not have
• Sandwich menus

```html
<!DOCTYPE html>
<html lang="en">
<head>
<meta charset="UTF-8">
<title>Lille Ro – Welcome</title>
<link rel="stylesheet" href="https://fonts.googleapis.com/css2?family=Figtree:wght@600;700;800&display=swap">
<style>
  :root {
    --purple-light: #8a6fa6;
    --purple-mid: #6e5487;
    --purple-deep: #574468;
    --mauve-low: #6a5466;
    --slate-base: #55505a;
    --white: #ffffff;
    --soft-white: #ece4f1;
    --orange: #faa54b;
    --note-grey: rgba(225, 220, 230, 0.62);
  }
  * { margin: 0; padding: 0; box-sizing: border-box; }
  html, body {
    width: 675px;
    height: 1200px;
    overflow: hidden;
  }
  body {
    font-family: "Figtree", sans-serif;
    background: var(--slate-base);
  }
  .welcome-screen {
    position: relative;
    width: 675px;
    height: 1200px;
    overflow: hidden;
    text-align: center;
  }
  .backdrop-photo {
    position: absolute;
    inset: 0;
    background:
      radial-gradient(ellipse 260px 320px at 470px 330px, rgba(140, 110, 160, 0.55), transparent 70%),
      radial-gradient(ellipse 300px 260px at 150px 260px, rgba(160, 135, 180, 0.5), transparent 70%),
      radial-gradient(ellipse 380px 240px at 380px 760px, rgba(90, 70, 100, 0.45), transparent 70%),
      linear-gradient(180deg, var(--purple-light) 0%, var(--purple-mid) 35%, var(--purple-deep) 55%, var(--mauve-low) 78%, var(--slate-base) 100%);
  }
  .brand-mark {
    position: absolute;
    top: 268px;
    left: 0;
    width: 100%;
    display: flex;
    align-items: center;
    justify-content: center;
    gap: 14px;
    color: var(--white);
    font-weight: 700;
    font-size: 44px;
    letter-spacing: 0.5px;
  }
  .brand-mark .brand-dot {
    width: 22px;
    height: 22px;
    border-radius: 50%;
    background: var(--white);
  }
  .app-title {
    position: absolute;
    top: 506px;
    width: 100%;
    color: var(--white);
    font-weight: 700;
    font-size: 31px;
  }
  .app-tagline {
    position: absolute;
    top: 572px;
    width: 100%;
    color: var(--soft-white);
    font-weight: 700;
    font-size: 23px;
  }
  .begin-button {
    position: absolute;
    top: 766px;
    left: 0;
    width: 100%;
    background: none;
    border: 0;
    color: var(--orange);
    font-family: "Figtree", sans-serif;
    font-weight: 800;
    font-size: 142px;
    line-height: 1;
    letter-spacing: 1px;
    cursor: pointer;
  }
  .health-note {
    position: absolute;
    top: 1040px;
    left: 0;
    width: 100%;
    color: var(--note-grey);
    font-weight: 700;
    font-size: 23px;
    line-height: 33px;
  }
</style>
</head>
<body>
  <main class="welcome-screen">
    <div class="backdrop-photo" role="img" aria-label="Softly blurred photo of a parent holding a baby, tinted purple"></div>

    <div class="brand-mark">
      <span class="brand-dot"></span>
      <span class="brand-name">Lille Ro</span>
    </div>

    <h1 class="app-title">Lille Ro</h1>
    <p class="app-tagline">Help relieve your child balance</p>

    <button class="begin-button" type="button">BEGIN</button>

    <p class="health-note">Always consult a physician if you suspect your child<br>is in need of health care. See FAQ for more info.</p>
  </main>
</body>
</html>
```